Updated front page of Brochure Design

We need to upgrade the front page of our brochure to include all that we offer our clients and I would like this expressed visually. Basically people think that we just supply packaging machinery, and we do a lot more than that. The services that we offer that need to be represented on the cover include (these could be in the form of modern icons as a suggestion): Automated Packaging Equipment – Robotic Solutions – Line Integration – Turnkey Solutions – Facility Design - Service Team – Ongoing Support (these icons have been uploaded for use)

Other wording to be on cover: A holistic approach to your packaging line.

The design needs to be inline with current branding and colours. I have attached our branding identity, current corporate brochure, product brochure for reference and the link to website is www.corvanta-pack.example (do not contact us outside of this medium as we will not respond)

Examples are attached

Target Market(s)

Manufacturers of food and beverage, FMCG etc

Industry/Entity Type

Manufacturing

Requirements
Must have
• Logo
• Simple, clever, sophisticated design
• Brand colours

```html
<!DOCTYPE html>
<html lang="en">
<head>
<meta charset="utf-8">
<title>Corvanta Pack – Brochure Cover</title>
<link rel="stylesheet" href="https://fonts.googleapis.com/css2?family=Saira:wght@500;700&family=Arimo:wght@400&display=swap">
<style>
  :root{
    --stage:#2b2c2e;
    --paper-light:#f1f1f2;
    --paper-mid:#dcdcde;
    --tile-black:#161616;
    --line-white:#ffffff;
    --brand-blue:#1f2a8e;
    --brand-orange:#f5a21b;
    --ink:#1b1b1b;
    --heading-grey:#2a2a2a;
  }
  html,body{margin:0;padding:0;width:1200px;height:1200px;overflow:hidden;background:var(--stage);}
  .cover{position:absolute;left:175px;top:0;width:849px;height:1200px;}
  .cover svg{display:block;width:100%;height:100%;}
  .heading-kicker{font-family:'Saira',sans-serif;font-weight:500;fill:var(--heading-grey);}
  .heading-main{font-family:'Saira',sans-serif;font-weight:700;fill:var(--brand-blue);}
  .brand-name{font-family:'Saira',sans-serif;font-weight:700;fill:var(--ink);}
  .tagline{font-family:'Arimo',sans-serif;font-weight:400;}
  .tagline .blue{fill:var(--brand-blue);}
  .tagline .orange{fill:var(--brand-orange);}
  .tile{fill:var(--tile-black);}
  .tile-edge{fill:none;stroke:var(--line-white);stroke-width:2;}
  .icon-ring{fill:none;stroke:var(--line-white);stroke-width:3;}
  .icon-line{fill:none;stroke:var(--line-white);stroke-width:4;stroke-linecap:round;stroke-linejoin:round;}
  .icon-fill{fill:var(--line-white);}
</style>
</head>
<body>
<div class="cover">
<svg viewBox="235 22 1030 1456" preserveAspectRatio="none" xmlns="http://www.w3.org/2000/svg">
  <defs>
    <linearGradient id="paper" x1="0" y1="0" x2="1" y2="1">
      <stop offset="0" stop-color="#e6e6e8"/>
      <stop offset="0.5" stop-color="#f2f2f3"/>
      <stop offset="1" stop-color="#d9d9db"/>
    </linearGradient>
    <linearGradient id="scene" x1="0.1" y1="0" x2="0.9" y2="1">
      <stop offset="0" stop-color="#1a1a1a"/>
      <stop offset="0.35" stop-color="#5a5c5e"/>
      <stop offset="0.7" stop-color="#d8d8d8"/>
      <stop offset="1" stop-color="#f4f4f4"/>
    </linearGradient>
  </defs>

  <!-- paper -->
  <rect class="paper" x="235" y="22" width="1030" height="1456" fill="url(#paper)"/>
  <g class="facets" fill="#ffffff" opacity="0.35">
    <polygon points="235,22 700,22 450,420"/>
    <polygon points="900,22 1265,22 1265,520"/>
    <polygon points="235,450 600,560 235,700"/>
    <polygon points="800,420 1265,300 1265,700"/>
    <polygon points="235,1100 500,1300 235,1440"/>
  </g>

  <!-- heading -->
  <text class="heading-kicker" x="315" y="304" font-size="48" textLength="738" lengthAdjust="spacingAndGlyphs">A HOLISTIC APPROACH TO YOUR</text>
  <text class="heading-main" x="318" y="400" font-size="104" textLength="862" lengthAdjust="spacingAndGlyphs">PACKAGING LINE</text>

  <!-- facility scene area -->
  <path role="img" aria-label="3D render of a packaging facility floor with forklifts, conveyors and racking"
        d="M365,575 L748,575 L1005,830 L748,1086 L620,958 L365,702 Z" fill="url(#scene)"/>

  <!-- dark tiles -->
  <polygon class="tile" points="235,575 365,575 362,702 235,830"/>
  <polygon class="tile" points="235,830 362,958 235,1086"/>
  <polygon class="tile" points="362,702 490,830 362,958 235,830"/>
  <polygon class="tile" points="492,830 620,958 492,1086 364,958"/>
  <polygon class="tile" points="620,958 748,1086 620,1214 492,1086"/>
  <polygon class="tile" points="876,958 1004,1086 876,1214 748,1086"/>
  <polygon class="tile" points="1134,702 1262,830 1134,958 1006,830"/>
  <polygon class="tile" points="1134,958 1262,1086 1134,1214 1006,1086"/>
  <polygon class="tile" points="1005,1086 1133,1214 1005,1342 877,1214"/>

  <!-- tile edges -->
  <g class="tile-edge">
    <polyline points="235,830 362,702 490,830 620,958 748,1086"/>
    <polyline points="235,830 362,958 490,830"/>
    <polyline points="362,958 492,1086 620,958"/>
    <polyline points="492,575 748,830 876,702"/>
    <polyline points="620,702 748,575"/>
    <polyline points="492,830 748,575"/>
    <polyline points="620,958 876,702"/>
    <polyline points="748,1086 876,958 1004,1086 876,1214"/>
    <polyline points="1006,830 1134,958 1262,830"/>
    <polyline points="1006,1086 1134,958"/>
    <polyline points="1005,1086 1133,1214"/>
    <polyline points="877,1214 1005,1086"/>
  </g>

  <!-- icons -->
  <g class="icon factory" transform="translate(362,830)">
    <circle class="icon-ring" r="51"/>
    <path class="icon-fill" d="M-32,20 L-32,-4 L-18,-14 L-18,-4 L-4,-14 L-4,-4 L10,-14 L10,-30 L18,-30 L18,20 Z"/>
    <rect class="icon-fill" x="22" y="-6" width="12" height="26"/>
  </g>
  <g class="icon service" transform="translate(492,958)">
    <circle class="icon-ring" r="51"/>
    <circle class="icon-line" r="14"/>
    <circle class="icon-fill" r="5"/>
    <path class="icon-line" d="M-14,-24 L-24,-14 M14,24 L24,14 M-14,24 L-24,14 M14,-24 L24,-14"/>
    <path class="icon-line" d="M12,12 L28,30"/>
  </g>
  <g class="icon integration" transform="translate(620,1086)">
    <circle class="icon-ring" r="51"/>
    <circle class="icon-line" cx="-12" cy="12" r="13"/>
    <circle class="icon-line" cx="14" cy="-12" r="13"/>
    <path class="icon-line" d="M-30,30 L-12,12 M-12,12 L-12,22 M-12,12 L-22,12"/>
    <path class="icon-line" d="M30,-30 L14,-12 M14,-12 L24,-12 M14,-12 L14,-22"/>
  </g>
  <g class="icon robotics" transform="translate(1134,830)">
    <circle class="icon-ring" r="51"/>
    <rect class="icon-fill" x="-16" y="22" width="32" height="8"/>
    <path class="icon-line" d="M0,22 L0,4 L-16,-18 L12,-28 L20,-18"/>
    <circle class="icon-fill" cx="-16" cy="-18" r="6"/>
    <circle class="icon-fill" cx="0" cy="4" r="6"/>
  </g>
  <g class="icon facility-design" transform="translate(876,1086)">
    <circle class="icon-ring" r="51"/>
    <rect class="icon-line" x="-30" y="-22" width="44" height="30"/>
    <path class="icon-line" d="M-30,26 L14,26 M-22,18 L-22,26"/>
    <circle class="icon-fill" cx="24" cy="-4" r="9"/>
    <path class="icon-fill" d="M10,26 Q24,4 38,26 Z"/>
  </g>
  <g class="icon support" transform="translate(1134,1086)">
    <circle class="icon-ring" r="51"/>
    <path class="icon-line" d="M-9,14 Q-18,4 -16,-6 A16,16 0 1 1 16,-6 Q18,4 9,14 Z"/>
    <path class="icon-line" d="M-7,22 L7,22 M-5,28 L5,28"/>
    <path class="icon-line" d="M0,-36 L0,-30 M-24,-26 L-20,-22 M24,-26 L20,-22 M-32,-4 L-26,-4 M32,-4 L26,-4"/>
  </g>
  <g class="icon turnkey" transform="translate(1005,1214)">
    <circle class="icon-ring" r="51"/>
    <path class="icon-line" d="M-24,-8 L0,-20 L24,-8 L24,18 L0,30 L-24,18 Z M-24,-8 L0,4 L24,-8 M0,4 L0,30"/>
    <path class="icon-line" d="M-12,-14 L12,-2 M12,-14 L-12,-2"/>
  </g>

  <!-- brand -->
  <rect x="320" y="1300" width="42" height="74" fill="var(--brand-blue)"/>
  <text class="brand-name" x="380" y="1332" font-size="44" textLength="366" lengthAdjust="spacingAndGlyphs">CORVANTA PACK</text>
  <text class="tagline" x="380" y="1362" font-size="21"><tspan class="blue">Engineering Excellence.</tspan><tspan class="orange" dx="8">Since 1926.</tspan></text>

  <!-- base band -->
  <rect x="235" y="1446" width="1030" height="32" fill="var(--tile-black)"/>
</svg>
</div>
</body>
</html>
```